Help our Crumb Parlour find our winning design! We're looking for a business card....

We’re a Crumb Parlour in NY specializing in custom-made cakes and unique desserts.
Our cakes combine flavor and art, each designed to match customer’s special event and theme.
We’d like a unique business card with a clean design that will combine French chic and artistic look & feel.
We’d like to differentiate ourselves from standard bakeries, please don’t offer cupcake images :-)
Our logo is peach-pink and brown and we’d love to use these colors ( . Another color that can be added is gold - or feel free to suggest!

Target Market(s)

Women, ages 25-55

Industry/Entity Type

Boutique

Contact Information for Business Card

Text on card:
Logo
Crumb Parlour by Dana Whitfield

www.xxxxxxxx.com
xxx@xxxxx.com
(516) xxx-xxxx
F – xxxxxxxxxx
IG - xxxxxxxxx

Font styles to use
Sans Serif
Script

Requirements
Must have
• Logo
• Clean look
• French chic and artistic look & feel.
Nice to have
• Damask pattern
Should not have
• Cupcake images

```html
<!DOCTYPE html>
<html lang="en">
<head>
<meta charset="utf-8">
<title>Crumb Parlour – Business Card</title>
<link rel="stylesheet" href="https://fonts.googleapis.com/css2?family=Cormorant+Garamond:wght@500;600&family=Libre+Baskerville:wght@700&family=Montserrat:wght@500&display=swap">
<style>
  :root {
    --stage: #d9d9d9;
    --blush: #ecdcdc;
    --blush-deep: #e2cfcf;
    --cocoa: #2e1d1b;
    --gold: #e6cf86;
    --peach: #f0a08c;
    --ink: #2a1a18;
  }
  * { box-sizing: border-box; margin: 0; padding: 0; }
  html, body { width: 1200px; height: 900px; overflow: hidden; }
  body {
    background: var(--stage);
    position: relative;
    font-family: "Cormorant Garamond", serif;
  }
  .card {
    position: absolute;
    left: 220px;
    width: 760px;
    height: 400px;
    overflow: hidden;
    box-shadow: 0 6px 18px rgba(0,0,0,.18);
  }
  .card--front { top: 40px; }
  .card--back { top: 460px; }

  .card__pattern {
    position: absolute; inset: 0;
    background: radial-gradient(ellipse at center, var(--blush) 0%, var(--blush-deep) 100%);
  }
  .band {
    position: absolute; left: 0; right: 0;
    background: var(--cocoa);
  }
  .band--top-front { top: 0; height: 34px; border-bottom: 3px solid var(--gold); }
  .band--contact {
    top: 262px; height: 86px;
    border-top: 3px solid var(--gold);
    display: flex; align-items: center;
    padding: 0 36px;
    color: var(--gold);
    white-space: nowrap;
  }
  .band--top-back { top: 0; height: 30px; border-bottom: 3px solid var(--gold); }
  .band--bottom-back { bottom: 0; height: 62px; border-top: 3px solid var(--gold); }

  .brand {
    position: absolute; left: 0; right: 0;
    display: flex; flex-direction: column; align-items: center;
  }
  .card--front .brand { top: 110px; }
  .card--back .brand { top: 70px; }
  .brand__name {
    display: flex; align-items: center; gap: 14px;
    font-family: "Cormorant Garamond", serif;
    font-weight: 600;
    font-size: 64px;
    line-height: 1;
    color: var(--ink);
    white-space: nowrap;
  }
  .brand__dot {
    width: 16px; height: 16px; border-radius: 50%;
    background: var(--peach);
  }
  .brand__tagline {
    margin-top: 14px;
    font-family: "Montserrat", sans-serif;
    font-weight: 500;
    font-size: 15px;
    letter-spacing: .32em;
    color: var(--ink);
    white-space: nowrap;
  }

  .contact__name {
    font-size: 23px; font-weight: 600; letter-spacing: .08em;
    margin-right: auto;
    flex-shrink: 0;
  }
  .contact__item {
    display: flex; align-items: center; gap: 9px;
    font-size: 17px; font-weight: 500;
    font-variant-numeric: lining-nums;
    margin-left: 32px;
    flex-shrink: 0;
  }
  .contact__icon {
    width: 20px; height: 20px;
    flex-shrink: 0;
  }

  .details {
    position: absolute; left: 0; right: 0; top: 200px;
    text-align: center;
    font-family: "Libre Baskerville", serif;
    font-weight: 700;
    font-size: 22px;
    line-height: 1.45;
    color: var(--ink);
    white-space: nowrap;
  }
  .details__social { color: var(--peach); }
</style>
</head>
<body>

  <section class="card card--front">
    <div class="card__pattern" role="img" aria-label="Soft blush damask pattern background"></div>
    <div class="band band--top-front"></div>
    <div class="brand">
      <div class="brand__name"><span class="brand__dot"></span>Velvet Hours</div>
      <div class="brand__tagline">HANDCRAFTED WITH LOVE</div>
    </div>
    <div class="band band--contact">
      <span class="contact__name">DANA WHITFIELD</span>
      <span class="contact__item">
        <svg class="contact__icon" viewBox="0 0 22 22" aria-hidden="true">
          <circle cx="11" cy="11" r="10" fill="none" stroke="currentColor" stroke-width="1.4"/>
          <rect x="7.5" y="5.5" width="7" height="11" rx="1.2" fill="none" stroke="currentColor" stroke-width="1.3"/>
          <line x1="10" y1="14.5" x2="12" y2="14.5" stroke="currentColor" stroke-width="1.3"/>
        </svg>
        (516) 555-0192
      </span>
      <span class="contact__item">
        <svg class="contact__icon" viewBox="0 0 22 22" aria-hidden="true">
          <circle cx="11" cy="11" r="10" fill="none" stroke="currentColor" stroke-width="1.4"/>
          <rect x="5.5" y="7.5" width="11" height="7" fill="none" stroke="currentColor" stroke-width="1.3"/>
          <polyline points="5.5,7.5 11,11.5 16.5,7.5" fill="none" stroke="currentColor" stroke-width="1.3"/>
        </svg>
        dana@VelvetHoursNY.com
      </span>
    </div>
  </section>

  <section class="card card--back">
    <div class="card__pattern" role="img" aria-label="Soft blush damask pattern background"></div>
    <div class="band band--top-back"></div>
    <div class="brand">
      <div class="brand__name"><span class="brand__dot"></span>Velvet Hours</div>
      <div class="brand__tagline">HANDCRAFTED WITH LOVE</div>
    </div>
    <div class="details">
      <p>Logo Crumb Parlour by Dana Whitfield</p>
      <p class="details__social">VelvetHoursNYCakes</p>
      <p>www.VelvetHoursNY.com</p>
    </div>
    <div class="band band--bottom-back"></div>
  </section>

</body>
</html>
```